Business Card Design

I would like a new business card that incorporates the new colors and font of the attached DKM4x10.pdf file of our new sign (latte & luxurious red from Kelvane Fairbrook colors) with the logo from the old business card (file name is New2014.pdf). You can remove the phrases from the old card, and just use the contact info provided above. Please let me know if you have any questions.

Industry/Entity Type

Business

Contact Information for Business Card

Dana Kay Morrow, LLC
Real Estate Attorney
842 Larkspur Street
Fernvale, KA 40218
(O) 555-203-4179
(C) 555-372-9051
dana@dkmlawoffice.com
dkmlawoffice.com

```html
<!DOCTYPE html>
<html lang="en">
<head>
<meta charset="utf-8">
<title>Dana Kay Morrow, LLC — Business Card</title>
<link href="https://fonts.googleapis.com/css2?family=Rokkitt:wght@700;800&family=Libre+Caslon+Text&family=Libre+Baskerville:wght@700&family=Arimo&display=swap" rel="stylesheet">
<style>
  :root {
    --luxurious-red: #a62a32;
    --latte-light: #f1e5d8;
    --latte-edge: #edc99c;
    --ink: #111111;
    --page: #ffffff;
  }
  html, body {
    margin: 0;
    width: 1200px;
    height: 1200px;
    overflow: hidden;
    background: var(--page);
  }
  .card {
    position: absolute;
    left: 0;
    top: 267px;
    width: 1200px;
    height: 666px;
    display: block;
  }
  .name { font-family: "Rokkitt", serif; font-weight: 800; fill: var(--luxurious-red); }
  .entity { font-family: "Rokkitt", serif; font-weight: 800; fill: var(--luxurious-red); }
  .title { font-family: "Rokkitt", serif; font-weight: 800; fill: var(--luxurious-red); }
  .tagline { font-family: "Libre Caslon Text", serif; fill: var(--luxurious-red); }
  .address { font-family: "Libre Baskerville", serif; font-weight: 700; fill: var(--luxurious-red); }
  .contact { font-family: "Arimo", sans-serif; fill: var(--ink); }
</style>
</head>
<body>
<svg class="card" viewBox="0 0 1223 679" xmlns="http://www.w3.org/2000/svg" role="img" aria-label="Business card for Dana Kay Morrow, LLC, Real Estate Attorney">
  <defs>
    <radialGradient id="latte" cx="50%" cy="50%" r="75%">
      <stop offset="0%" stop-color="#f1e5d8"/>
      <stop offset="60%" stop-color="#f1e5d8"/>
      <stop offset="100%" stop-color="#edc99c"/>
    </radialGradient>
    <filter id="soft-shadow" x="-20%" y="-20%" width="140%" height="140%">
      <feDropShadow dx="4" dy="4" stdDeviation="6" flood-color="#000" flood-opacity="0.25"/>
    </filter>
  </defs>

  <rect class="card-face" width="1223" height="679" fill="url(#latte)"/>

  <path class="accent-tab" filter="url(#soft-shadow)" fill="var(--luxurious-red)"
        d="M0 34 L290 208 Q345 242 318 300 L135 610 Q105 660 50 637 L0 612 Z"/>

  <text class="name" x="350" y="176" font-size="118" textLength="746" lengthAdjust="spacingAndGlyphs">Dana Kay Morrow</text>
  <text class="entity" x="1097" y="220" font-size="38" text-anchor="end" textLength="62" lengthAdjust="spacingAndGlyphs">LLC</text>
  <rect class="rule" x="500" y="216" width="443" height="3" fill="var(--luxurious-red)"/>

  <text class="title" x="722" y="284" font-size="44" text-anchor="middle" textLength="372" lengthAdjust="spacingAndGlyphs">Real Estate Attorney</text>
  <text class="tagline" x="726" y="352" font-size="46" text-anchor="middle" textLength="659" lengthAdjust="spacingAndGlyphs">Where it’s always closing time</text>
  <text class="address" x="729" y="413" font-size="29" text-anchor="middle" textLength="666" lengthAdjust="spacingAndGlyphs">842 Larkspur Street, Fernvale, KA 40218</text>
  <text class="contact" x="729" y="475" font-size="40" text-anchor="middle" textLength="671" lengthAdjust="spacingAndGlyphs">(O) 555-203-4179 Cell: 555-372-9051</text>
  <text class="contact" x="746" y="521" font-size="32" text-anchor="middle" textLength="560" lengthAdjust="spacingAndGlyphs">dana@dkmlawoffice.com  dkmlawoffice.com</text>
</svg>
</body>
</html>
```